Selam-Kaveh - Promote and Support a community

Design a website for Ethiopean Community. the design should be friendly, easy to navigate and maintain the look & feel of the Ethiopian culture. a proposed logo is attached but it can be change according to your recommendations. This is a project we are doing at a discount rate as it supports a weak community.
Please visit their current website http://www.selam-kaveh.example.org/index.php?lang=en

Target Market(s)

Community members, potential doners

Industry/Entity Type

community

Number of Pages Required

1 page

Font styles to use
Sans Serif

Requirements
Must have
• easy to navigate friendly interface

```html
<!DOCTYPE html>
<html lang="en">
<head>
<meta charset="utf-8">
<title>Selam-Kaveh</title>
<link rel="stylesheet" href="https://fonts.googleapis.com/css2?family=Montserrat:wght@300;400;500;700;800&display=swap">
<style>
  :root {
    --red: #e3201b;
    --ink: #2b2b2b;
    --muted: #6a6a6a;
    --white: #ffffff;
    --hero-dark: #4a3a33;
    --hero-mid: #8a6e60;
    --hero-light: #b59888;
  }
  * { margin: 0; padding: 0; box-sizing: border-box; }
  html, body { width: 1200px; height: 800px; overflow: hidden; background: var(--white); }
  body { font-family: "Montserrat", sans-serif; color: var(--ink); position: relative; }

  .site-header {
    position: absolute; top: 0; left: 0; width: 1200px; height: 100px;
    border-bottom: 2px solid var(--red); background: var(--white);
  }
  .brand {
    position: absolute; left: 150px; top: 34px;
    display: flex; align-items: center; gap: 10px;
  }
  .brand-dot { width: 28px; height: 28px; border-radius: 50%; background: var(--red); }
  .brand-name { font-size: 18px; font-weight: 700; color: var(--red); }

  .contact-icons {
    position: absolute; right: 160px; top: 22px; display: flex; gap: 5px;
  }
  .contact-icons span {
    width: 17px; height: 17px; border: 1.3px solid var(--ink); border-radius: 50%;
    display: flex; align-items: center; justify-content: center;
  }
  .main-nav {
    position: absolute; right: 160px; top: 58px; display: flex; gap: 21px;
    font-size: 12.5px; font-weight: 500;
  }
  .main-nav a { color: var(--ink); text-decoration: none; position: relative; }
  .main-nav a.is-active::after {
    content: ""; position: absolute; left: 0; right: 0; bottom: -4px; height: 2px; background: var(--red);
  }

  .hero {
    position: absolute; top: 102px; left: 0; width: 1200px; height: 426px;
    background: linear-gradient(110deg, var(--hero-dark) 0%, var(--hero-mid) 45%, var(--hero-light) 70%, var(--hero-mid) 100%);
  }
  .hero-shade { position: absolute; inset: 0; background: rgba(40, 28, 22, 0.35); }
  .hero-copy { position: absolute; left: 195px; top: 130px; }
  .hero-title { font-size: 41px; font-weight: 500; color: var(--red); letter-spacing: 1px; line-height: 1; }
  .hero-sub {
    margin-top: 10px; font-size: 24px; font-weight: 300; color: var(--white);
    letter-spacing: 0.5px; line-height: 1.5;
  }
  .hero-btn {
    margin-top: 22px; display: inline-flex; height: 36px; background: var(--red); color: var(--white);
    font-size: 11px; font-weight: 500; text-decoration: none;
  }
  .hero-btn .label { padding: 0 20px; display: flex; align-items: center; }
  .hero-btn .arrow { width: 36px; display: flex; align-items: center; justify-content: center; border-left: 1px solid rgba(255,255,255,0.5); }

  .welcome { position: absolute; top: 528px; left: 0; width: 1200px; height: 272px; text-align: center; }
  .welcome-kicker { margin-top: 46px; font-size: 27px; font-weight: 400; letter-spacing: 1px; }
  .welcome-name { font-size: 27px; font-weight: 800; color: var(--red); letter-spacing: 1px; line-height: 1.2; }
  .welcome-rule { width: 30px; height: 4px; margin: 14px auto 0; border: 1px solid var(--muted); border-radius: 2px; }
  .welcome-cols {
    display: flex; gap: 40px; width: 730px; margin: 22px auto 0; text-align: justify;
    font-size: 10px; line-height: 1.7; color: var(--muted);
  }
  .welcome-cols p { flex: 1; }
</style>
</head>
<body>
  <header class="site-header">
    <div class="brand">
      <span class="brand-dot"></span>
      <span class="brand-name">Selam-Kaveh</span>
    </div>
    <div class="contact-icons">
      <span>
        <svg width="9" height="9" viewBox="0 0 24 24"><path d="M6.6 10.8a15 15 0 0 0 6.6 6.6l2.2-2.2c.3-.3.7-.4 1-.2 1.1.4 2.3.6 3.6.6.6 0 1 .4 1 1V20c0 .6-.4 1-1 1A17 17 0 0 1 3 4c0-.6.4-1 1-1h3.5c.6 0 1 .4 1 1 0 1.3.2 2.5.6 3.6.1.3 0 .7-.2 1z" fill="#2b2b2b"/></svg>
      </span>
      <span></span>
      <span></span>
    </div>
    <nav class="main-nav">
      <a href="#" class="is-active">Home</a>
      <a href="#">About</a>
      <a href="#">The Community</a>
      <a href="#">Programs</a>
      <a href="#">News</a>
      <a href="#">Advocacy</a>
      <a href="#">Partners</a>
      <a href="#">Support Us</a>
    </nav>
  </header>

  <section class="hero">
    <div class="hero-shade" role="img" aria-label="Photo of many hands of different skin tones stacked together in unity"></div>
    <div class="hero-copy">
      <h1 class="hero-title">DEDICATED</h1>
      <p class="hero-sub">TO IMPROVING THE HEALTH<br>OF THE ETHIOPIAN ISRAELI COMMUNITY</p>
      <a href="#" class="hero-btn"><span class="label">Read More</span><span class="arrow">&rsaquo;</span></a>
    </div>
  </section>

  <section class="welcome">
    <p class="welcome-kicker">Welcome to</p>
    <h2 class="welcome-name">Selam-Kaveh</h2>
    <div class="welcome-rule"></div>
    <div class="welcome-cols">
      <p>Aliyah (immigration) from Ethiopia to Israel and the transition to a sedentary lifestyle has resulted in the emergence of chronic diseases, in particular diabetes. While only 0.4% of the new immigrants were diagnosed with Type 2 diabetes upon arrival, by the time they had lived in Israel for ten years the figure had risen to 18%.</p>
      <p>Selam-Kaveh has developed into a small but dedicated NGO, delivering services throughout Israel with the backing and cooperation of a wide range of local and national bodies, including the Ministry of Health, the Ministry of Welfare, local councils, health funds and community groups working together for lasting change.</p>
    </div>
  </section>
</body>
</html>
```